Package of web graphics needed

Utilizing a recently selected logo from a Pixel Harbor contest, we need to have some ads, fb cover, home page slide image created for our new 877-Toll-Free Number Product. Please feel free to check our site at www.ringvantagehub.com

You'll find attached the 877 toll free logo in 2 layouts.

Here are the ads and dimensions of each that are needed:
1.)Banners/ads - 468x60
468×60 px
125×125 px
120×600 px
120x90 px
88×31 px button
5.)FB Cover - 851 x 315
6.)Home page slider image - 944 x 328

Here is the text & some ideas to use for these. Feel free to use different versions depending on which ad they work better on:
-

Market Your Business in a Memorable Way – Pre-Order Yours Today, Deadline: Dec. 7th
[include logo]
-
[RingVantage] Don't Miss out on your chance to finally get a great vanity!

Order Yours Today
-

Don't Miss out on your chance to finally get a great vanity!
Dec. 7th Deadline to pre-order

Don't Ignore 877!– The newest toll free prefix – Coming Dec. 7th – Get Yours Today

FB COVER guidelines -
Requirements:
Include the logo
Limited Time Left – Get your Reservation in by December 7th

HOME PAGE Image Slide:
Use the logo,

Couple of Ideas we're interested in seeing:

[Billboard sign stock image … with the number 877-Grab-ONE on the billboard]
[RingVantage and caricature] [1 caricature looking surprised]

```html
<!DOCTYPE html>
<html lang="en">
<head>
<meta charset="utf-8">
<title>RingVantage – Home Page Slide</title>
<link rel="stylesheet" href="https://fonts.googleapis.com/css2?family=Montserrat:wght@800&display=swap">
<style>
  :root {
    --canvas-bg: #232323;
    --sky-deep: #0a6fd6;
    --sky-mid: #2f97e6;
    --board-frame: #b9bec4;
    --board-face: #f2f3f5;
    --board-white: #ffffff;
    --brand-navy: #0f3466;
    --brand-green: #6abf3f;
  }
  * { margin: 0; padding: 0; box-sizing: border-box; }
  html, body {
    width: 1200px;
    height: 750px;
    overflow: hidden;
    background: var(--canvas-bg);
  }
  .slide {
    position: absolute;
    left: 128px;
    top: 211px;
    width: 944px;
    height: 328px;
    overflow: hidden;
  }
  .slide-scene {
    position: absolute;
    inset: 0;
    background:
      linear-gradient(115deg, transparent 55%, rgba(255,255,255,0.35) 80%, rgba(255,255,255,0.55) 100%),
      linear-gradient(180deg, var(--sky-deep) 0%, var(--sky-mid) 60%, #1a7fd8 100%);
  }
  .billboard {
    position: absolute;
    left: 126px;
    top: 41px;
    width: 676px;
    height: 226px;
    background: var(--board-frame);
    padding: 4px;
  }
  .billboard-face {
    position: relative;
    width: 100%;
    height: 100%;
    background: linear-gradient(100deg, var(--board-face) 0%, var(--board-white) 60%, var(--board-face) 100%);
  }
  .brand-panel {
    position: absolute;
    left: 23px;
    top: 38px;
    width: 414px;
    height: 144px;
    background: var(--board-white);
    display: flex;
    align-items: center;
    justify-content: center;
    gap: 14px;
  }
  .brand-mark {
    width: 22px;
    height: 22px;
    background: var(--brand-navy);
  }
  .brand-name {
    font-family: "Montserrat", sans-serif;
    font-weight: 800;
    font-size: 40px;
    line-height: 1;
    color: var(--brand-navy);
  }
  .call-to-action {
    position: absolute;
    left: 457px;
    top: 46px;
    font-family: "Montserrat", sans-serif;
    font-weight: 800;
    font-size: 58px;
    line-height: 64px;
  }
  .call-to-action .cta-verb { display: block; color: var(--brand-navy); }
  .call-to-action .cta-object { display: block; color: var(--brand-green); }
</style>
</head>
<body>
  <main class="slide">
    <div class="slide-scene" role="img" aria-label="Blue city skyline with a road and a billboard structure with lamps, walkway and pole"></div>
    <section class="billboard">
      <div class="billboard-face">
        <div class="brand-panel">
          <span class="brand-mark"></span>
          <span class="brand-name">RingVantage</span>
        </div>
        <p class="call-to-action">
          <span class="cta-verb">GRAB</span>
          <span class="cta-object">ONE</span>
        </p>
      </div>
    </section>
  </main>
</body>
</html>
```